Blockchain - Velmora Stake Pool

We need a website freshup for our velmora staking pool (coinnest7.com).
Goal would be to add couple of nice features for example like Pool Stats from K7Q (https://nodewatchers.net/pool/e7f31d0a9c4b62e8f0d7a1c93b5e48f2d06a7c19b3e85f4d27c0a6b91), and built it more user friendly and simple. A newcomer to crypto should be able to understand what staking is and how to go ahead to stake with K7Q.

Facts about us and K7Q:
We have two Nodes in Switzerland and one Node in Canada
• Active in the Velmora Eco System since QRB launch (Verified QRB Ticker)
• Team of 3 hard working guys of dedicated crypto/velmora fanboys since 2016
• Direct communication channel in Chatterly with commitment to educate newbies in the crypto and velmora universe- shoot your Questions

What is VLR and Staking ?
Vlr held on the Velmora network represents a stake in the network, with the size of the stake proportional to the amount of vlr held. The ability to delegate or pledge a stake is fundamental to how Velmora works. The amount of stake delegated to a given stake pool is the primary way protocol chooses who should add the next block to the blockchain, and receive a monetary reward for doing so.

The more stake is delegated to a stake pool (up to a certain point), the more likely it is to make the next block – and the rewards that it earns are shared between everyone who delegated their stake to that stake pool.
Updates

Target Market(s)

Global

Industry/Entity Type

Technical

Coding

Coded - Design and coding required

Number of Pages Required

1 page

Requirements
Must have
• Pool Info (Name, ID, Fees)
Instruction on what is staking and how it works (https://velmora.org/stake-pool-operation#faq) - Step by Step instruction
Link to chatterly group
About us
Responsive Design
HTML & CSS Files
Nice to have
• Pool Stats from K7Q (https://nodewatchers.net/pool/e7f31d0a9c4b62e8f0d7a1c93b5e48f2d06a7c19b3e85f4d27c0a6b91)
Little Map with Server Location
Animated background

```html
<!DOCTYPE html>
<html lang="en">
<head>
<meta charset="utf-8">
<title>Velmora Staking Pool – coinnest7.com</title>
<link href="https://fonts.googleapis.com/css2?family=Abril+Fatface&family=Libre+Franklin:wght@400;500;600;700&family=Poppins:wght@500;600;700&display=swap" rel="stylesheet">
<style>
:root{
  --navy:#0a1a2e;
  --navy-deep:#050d1a;
  --blue:#1536c8;
  --blue-bright:#1f4fe0;
  --ink:#222;
  --body:#3a3a3a;
  --muted:#666;
  --paper:#ffffff;
  --mist:#f4f0f0;
  --rule:#d8d4d4;
  --footer:#2c2c2c;
  --map-green:#8fc79a;
}
*{box-sizing:border-box;margin:0;padding:0}
html,body{width:1200px;height:3992px;overflow:hidden;background:var(--paper)}
body{font-family:"Libre Franklin",Arial,sans-serif;color:var(--body)}
.page{position:relative;width:1200px;height:3992px;overflow:hidden}
a{color:inherit;text-decoration:none}

/* header / hero */
.hero{position:absolute;left:0;top:0;width:1200px;height:648px;
  background:radial-gradient(ellipse at 55% 40%,#1d3a5c 0%,#0d2038 45%,var(--navy-deep) 100%)}
.brand{position:absolute;display:flex;align-items:center;gap:12px;color:#fff;
  font-family:"Libre Franklin",Arial,sans-serif;font-weight:600;letter-spacing:.5px}
.brand-mark{width:40px;height:40px;border:2px solid #fff;border-radius:50%}
.hero .brand{left:132px;top:44px;font-size:20px}
.nav{position:absolute;display:flex;gap:38px;color:#fff;font-weight:600;font-size:15px;letter-spacing:.5px}
.hero .nav{right:134px;top:36px}
.hero-title{position:absolute;left:0;width:1200px;top:255px;text-align:center;color:#fff;
  font-family:"Abril Fatface",Georgia,serif;font-size:50px;font-weight:400}
.btn-outline{position:absolute;border:2px solid #fff;color:#fff;font-weight:700;font-size:15px;
  letter-spacing:.5px;display:flex;align-items:center;justify-content:center}
.hero .btn-outline{left:536px;top:342px;width:128px;height:38px}
.slider-dots{position:absolute;left:570px;top:606px;display:flex;gap:8px}
.slider-dots span{width:5px;height:5px;border-radius:50%;background:#fff}
.slider-dots span.active{background:#8fd24a}

/* intro */
.intro{position:absolute;left:0;top:648px;width:1200px;height:449px;background:var(--paper)}
.intro-mark{position:absolute;left:150px;top:120px;width:300px;height:200px;display:flex;
  flex-direction:column;align-items:center;justify-content:center;gap:16px;color:var(--blue);
  font-family:"Poppins",Arial,sans-serif;font-weight:600;font-size:26px}
.intro-mark .dot{width:70px;height:70px;border:6px solid var(--blue);border-radius:50%}
.intro-divider{position:absolute;left:512px;top:57px;width:1px;height:334px;background:var(--rule)}
.intro-copy{position:absolute;left:600px;top:50px;width:475px}
.h-section{font-family:"Poppins",Arial,sans-serif;font-weight:700;color:var(--ink)}
.intro-copy h2{font-size:22px;padding-bottom:10px;border-bottom:2px solid #444;display:inline-block;margin-bottom:26px}
.intro-copy p{font-size:15.5px;line-height:24px;margin-bottom:24px}

/* stake pool explainer */
.explainer{position:absolute;left:0;top:1097px;width:1200px;height:1078px;background:var(--mist)}
.explainer h2{position:absolute;left:133px;top:48px;font-size:22px}
.rule-short{position:absolute;height:2px;width:62px;background:#888}
.explainer .intro-rule{left:133px;top:86px}
.explainer .lead{position:absolute;left:133px;top:112px;width:920px;font-size:15.5px;line-height:25px}
.explainer .lead p+p{margin-top:23px}
.explainer h3{position:absolute;left:0;width:1200px;top:304px;text-align:center;font-size:22px}
.explainer .center-rule{left:569px;top:343px}
.card{position:absolute;background:#fff;padding:38px 26px 20px 146px}
.card svg{position:absolute;left:44px;top:40px}
.card h4{font-family:"Poppins",Arial,sans-serif;font-weight:600;font-size:16.5px;color:var(--ink);margin-bottom:8px}
.card p{font-size:12.5px;line-height:17.6px;color:var(--body)}
.c1{left:136px;top:391px;width:456px;height:248px}
.c2{left:611px;top:391px;width:457px;height:248px}
.c3{left:136px;top:654px;width:456px;height:369px}
.c4{left:611px;top:654px;width:457px;height:369px}

/* setup */
.setup{position:absolute;left:0;top:2175px;width:1200px;height:465px;
  background:linear-gradient(100deg,#1846d8 0%,#1a4ee6 45%,#2a5cf0 70%,#1e47d6 100%)}
.setup-art{position:absolute;left:640px;top:0;width:560px;height:465px;
  background:radial-gradient(circle at 60% 50%,rgba(170,150,255,.45) 0%,rgba(120,110,240,.25) 35%,rgba(30,70,220,0) 70%)}
.setup h2{position:absolute;left:133px;top:56px;font-size:22px;color:#fff}
.setup .rule-short{left:133px;top:94px;background:#fff;width:40px}
.setup .copy{position:absolute;left:133px;top:122px;width:480px;color:#fff;font-size:15.5px;line-height:20.8px}
.setup .copy p+p{margin-top:20px}
.setup .btn-outline{left:133px;top:364px;width:117px;height:36px;font-size:14px}

/* pool stats */
.stats{position:absolute;left:0;top:2640px;width:1200px;height:592px;
  background:linear-gradient(135deg,#9fd0a6 0%,var(--map-green) 40%,#a7d3a5 70%,#93c89a 100%)}
.stats-panel{position:absolute;top:91px;height:416px;background:rgba(255,255,255,.9);padding:22px 22px 0}
.panel-left{left:229px;width:380px}
.panel-right{left:632px;width:355px}
.stat-row{display:flex;justify-content:space-between;align-items:center;height:33.8px;
  border-bottom:1px solid #e3e3e3;font-size:14px;color:var(--ink)}
.stat-row:last-child{border-bottom:none}
.stat-row .val{font-size:13px}
.stat-row .link{color:var(--blue);text-decoration:underline}
.stat-row .signup{color:var(--blue)}
.sat-bar{width:112px;height:6px;background:#c4c4c4;border-left:4px solid #555}

/* features */
.features{position:absolute;left:0;top:3232px;width:1200px;height:547px;background:#fff}
.feature{position:absolute;top:36px;height:464px;background:var(--mist);padding:30px 34px 0 36px}
.f1{left:132px;width:302px}
.f2{left:449px;width:301px}
.f3{left:766px;width:302px}
.feature .icon{width:86px;height:86px;border-radius:50%;background:var(--blue);display:flex;
  align-items:center;justify-content:center;margin-bottom:24px}
.feature h4{font-family:"Poppins",Arial,sans-serif;font-weight:600;font-size:16.5px;line-height:21px;color:var(--ink);margin-bottom:10px}
.feature p{font-size:12.5px;line-height:17.7px}

/* footer */
.site-footer{position:absolute;left:0;top:3779px;width:1200px;height:213px;background:var(--footer);color:#fff}
.site-footer .brand{left:134px;top:64px;font-size:20px}
.follow{position:absolute;right:132px;top:40px;display:flex;align-items:center;gap:10px;font-size:13px}
.follow .social{width:27px;height:27px;border-radius:50%;background:var(--blue-bright)}
.site-footer .nav{right:132px;top:100px;font-weight:500;font-size:15px;gap:36px}
.footer-rule{position:absolute;left:134px;top:138px;width:934px;height:1px;background:#666}
.copyright{position:absolute;right:132px;top:164px;font-size:12px;color:#ddd}
</style>
</head>
<body>
<div class="page">

  <header class="hero">
    <a class="brand" href="#"><span class="brand-mark"></span>VELMORA STAKING POOL</a>
    <nav class="nav"><a href="#">START</a><a href="#">ABOUT US</a><a href="#">SLA</a><a href="#">CREDITS</a></nav>
    <h1 class="hero-title">Blockchain Technology</h1>
    <a class="btn-outline" href="#">READ MORE</a>
    <div class="slider-dots"><span></span><span></span><span class="active"></span><span></span><span></span></div>
  </header>

  <section class="intro">
    <div class="intro-mark" role="img" aria-label="coinnest7 pool emblem"><span class="dot"></span>coinnest7</div>
    <div class="intro-divider"></div>
    <div class="intro-copy">
      <h2 class="h-section">What is VLR and Staking ?</h2>
      <p>Vlr held on the Velmora network represents a stake in the network, with the size of the stake proportional to the amount of vlr held. The ability to delegate or pledge a stake is fundamental to how Velmora works. The amount of stake delegated to a given stake pool is the primary way protocol chooses who should add the next block to the blockchain, and receive a monetary reward for doing so.</p>
      <p>The more stake is delegated to a stake pool (up to a certain point), the more likely it is to make the next block – and the rewards that it earns are shared between everyone who delegated their stake to that stake pool.</p>
    </div>
  </section>

  <section class="explainer">
    <h2 class="h-section">WHAT IS A STAKE POOL?</h2>
    <div class="rule-short intro-rule"></div>
    <div class="lead">
      <p>Stake pools may be either public or private. A public stake pool is a Velmora network node with a public address that other users can delegate to, and receive rewards. Private stake pools only deliver rewards to their owners.</p>
      <p>Stake pools are run by a reliable operator: an individual or business with the knowledge and resources to run the node on a consistent basis. Vlr holders can delegate to public stake pools if they wish to participate in the protocol and receive rewards, but do not wish to operate a Velmora network node themselves.</p>
    </div>
    <h3 class="h-section">HOW A USER CAN DELEGATE TO K7Q</h3>
    <div class="rule-short center-rule"></div>

    <article class="card c1">
      <svg width="70" height="72" viewBox="0 0 70 72" fill="none" stroke="#1536c8" stroke-width="4"><path d="M8 4h40v26M8 4v62h30"/><path d="M18 18h22M18 30h22M18 42h12"/><path d="M36 52l8 10 20-26"/></svg>
      <h4>Pledging Mechanism</h4>
      <p>While there is no required minimum pledge amount, pool operators can optionally pledge some or all of their stake to their pool to make their pool more attractive. The higher the amount of vlr pledged, the more rewards the pool will receive, which will attract more delegation. The a0 protocol parameter defines the influence of the pledge on the pool reward.</p>
    </article>
    <article class="card c2">
      <svg width="70" height="66" viewBox="0 0 70 66" fill="none" stroke="#1536c8" stroke-width="3.5"><rect x="4" y="40" width="8" height="22"/><rect x="22" y="32" width="8" height="30"/><rect x="40" y="38" width="8" height="24"/><rect x="58" y="26" width="8" height="36"/><path d="M8 24l18-12 18 8 18-16"/><circle cx="8" cy="24" r="3"/><circle cx="26" cy="12" r="3"/><circle cx="44" cy="20" r="3"/><circle cx="62" cy="4" r="3"/></svg>
      <h4>Desirability Index</h4>
      <p>The desirability of a pool is calculated by taking the pledged owner's stake, costs, and margin, and combining them with an influence from saturation and pool performance. This number will be used to rank pools in Harbor and Tessel, and indicates how ‘desirable’ or ‘attractive’ the pool is to potential delegators.</p>
    </article>
    <article class="card c3">
      <svg width="56" height="72" viewBox="0 0 56 72" fill="none" stroke="#1536c8" stroke-width="3"><path d="M4 4h34l14 14v50H4z"/><path d="M38 4v14h14"/><circle cx="22" cy="26" r="9"/><path d="M22 17v9h9"/><path d="M14 60v-6M22 60v-10M30 60v-14M38 60v-18M46 60v-22" stroke-width="3.5"/></svg>
      <h4>Saturation Parameter (K)</h4>
      <p>Saturation is a term used to indicate that a particular stake pool has more stake delegated to it than is ideal for the network, while k is the targeted number of desired pools. Once a pool reaches the point of saturation, it will offer diminishing rewards. The saturation mechanism was designed to prevent centralization by encouraging delegators to delegate to different stake pools, and to incentivize operators to set up alternative pools so that they can continue earning maximum rewards. Saturation, therefore, exists to preserve the interests of both vlr holders delegating their stake and stake pool operators, and to prevent any single pool from becoming too large.</p>
    </article>
    <article class="card c4">
      <svg width="78" height="78" viewBox="0 0 78 78" fill="none" stroke="#1536c8" stroke-width="3.5"><rect x="3" y="3" width="34" height="24"/><path d="M14 34h12"/><rect x="40" y="42" width="34" height="24"/><path d="M51 73h12"/><path d="M44 8h4M54 8h4M64 8h4M66 18v4M66 28v4M8 38v4M8 48v4M8 58h4M18 58h4M28 58h4" stroke-width="4"/></svg>
      <h4>Decentralization Parameter</h4>
      <p>This tunable parameter will control the ratio of slots created by the federation of nodes compared to those by stake pool nodes. It will be used at the beginning of Meridian’s deployment to the mainnet. It’s important to note that all rewards will be distributed to operating stake pools and none to the federated nodes during this transition period. The decentralization parameter is being implemented to allow the network to stabilize.</p>
    </article>
  </section>

  <section class="setup">
    <div class="setup-art" role="img" aria-label="Glowing coin imagery on a blue digital background"></div>
    <h2 class="h-section">How Do I Set Up A Stake Pool?</h2>
    <div class="rule-short"></div>
    <div class="copy">
      <p>It’s important to remember the role of a stake pool operator: to ensure reliable, 24/7 operation of a network node. As a stake pool operator, you have a responsibility to the vlr holders who delegate to you but also to the health of the network itself. This requires a stable and reliable network infrastructure and, ideally, system operation and server administration skills along with experience in development and operations.</p>
      <p>Anybody can learn how to operate a stake pool, but a degree of technical familiarity and knowledge is required.</p>
    </div>
    <a class="btn-outline" href="#">READ MORE</a>
  </section>

  <section class="stats" role="img" aria-label="Map showing server locations behind the pool statistics">
    <div class="stats-panel panel-left">
      <div class="stat-row"><span>Name</span><span class="val">coinnest7</span></div>
      <div class="stat-row"><span>Ticker</span><span class="val">K7Q</span></div>
      <div class="stat-row"><span>Website</span><span class="val link">https://coinnest7.com</span></div>
      <div class="stat-row"><span>Saturation</span><span class="sat-bar"></span></div>
      <div class="stat-row"><span>ROA (M)</span><span class="val">5.132%</span></div>
      <div class="stat-row"><span>ROA Lifetime</span><span class="val">6.212%</span></div>
      <div class="stat-row"><span>Live Stake</span><span class="val">790.97k</span></div>
      <div class="stat-row"><span>Active Stake</span><span class="val">785.26k</span></div>
      <div class="stat-row"><span>Pledge</span><span class="val">12.00k</span></div>
      <div class="stat-row"><span>Margin</span><span class="val">2%</span></div>
      <div class="stat-row"><span>Fixed Cost</span><span class="val">340</span></div>
    </div>
    <div class="stats-panel panel-right">
      <div class="stat-row"><span>Last Rewards</span><span class="val">E251</span></div>
      <div class="stat-row"><span>Estimated Blocks in Whole Epoch</span><span class="val">0.7</span></div>
      <div class="stat-row"><span>Block Trend</span><span class="val">0</span></div>
      <div class="stat-row"><span>Lifetime Blocks</span><span class="val">21</span></div>
      <div class="stat-row"><span>Lifetime Luck</span><span class="val">111%</span></div>
      <div class="stat-row"><span>Registered</span><span class="val">2020-08-03 11:04:51</span></div>
      <div class="stat-row"><span>Delegators</span><span class="val">19</span></div>
      <div class="stat-row"><span>Pool Owners</span><span class="val">1 (rewards)</span></div>
      <div class="stat-row"><span>Pledge Leverage</span><span class="val">65.9</span></div>
      <div class="stat-row"><span>Social Media</span><span class="val">none. add them</span></div>
      <div class="stat-row"><span>Claimed pool</span><span class="val signup">Sign Up</span></div>
    </div>
  </section>

  <section class="features">
    <article class="feature f1">
      <div class="icon"><svg width="52" height="52" viewBox="0 0 52 52" fill="none" stroke="#fff" stroke-width="3.5"><circle cx="26" cy="26" r="22"/><path d="M32 18c-2-3-12-4-12 2s12 4 12 11-10 6-13 2M26 12v28"/></svg></div>
      <h4>Fees</h4>
      <p>To enhance trust and satisfaction towards our delegators, at coinnest7.com cost transparency is key! In this sense, we always try to keep our fees at a minimum, with the target to maximise the profits of our delegators and to provide a performant Stake Pool. As a Stake Pool Operator, coinnest7.com charges a fee of 2.0% mainly used to cover our internal costs for infrastructure and security. The costs are continuously monitored to the developments of the Velmora Network to enable a healthy and competitive ecosystem.</p>
    </article>
    <article class="feature f2">
      <div class="icon"><svg width="44" height="52" viewBox="0 0 44 52" fill="#fff"><rect x="4" y="2" width="36" height="11" rx="2"/><rect x="4" y="16" width="36" height="11" rx="2"/><rect x="4" y="30" width="36" height="11" rx="2"/><rect x="20" y="41" width="4" height="7"/><rect x="2" y="47" width="40" height="3"/></svg></div>
      <h4>DDoS-Protected &amp;<br>99.9% Uptime</h4>
      <p>Our high performance server infrastructure offers the perfect basis to build a robust Stake Pool. It is equipped with SSD and DDOS attack protection and offers detailed monitoring. This trustworthy setup enables us to achieve an SLA of 99.95%</p>
    </article>
    <article class="feature f3">
      <div class="icon"><svg width="50" height="50" viewBox="0 0 50 50" fill="#fff"><path d="M21 2h8l1 7 5 2 6-4 6 6-4 6 2 5 7 1v8l-7 1-2 5 4 6-6 6-6-4-5 2-1 7h-8l-1-7-5-2-6 4-6-6 4-6-2-5-7-1v-8l7-1 2-5-4-6 6-6 6 4 5-2z"/><circle cx="25" cy="25" r="8" fill="#1536c8"/></svg></div>
      <h4>Swiss<br>Engineering</h4>
      <p>As a Swiss Stake Pool, coinnest7.com is committed to the motto "Made in Switzerland", quality and trust is therefore key. Accordingly, we are proud to provide a you with a geo-redundant Stakepool mainly hosted and maintained in Switzerland.</p>
    </article>
  </section>

  <footer class="site-footer">
    <div class="follow">Follow us <span class="social" aria-label="Social link"></span><span class="social" aria-label="Social link"></span><span class="social" aria-label="Social link"></span></div>
    <a class="brand" href="#"><span class="brand-mark"></span>VELMORA STAKING POOL</a>
    <nav class="nav"><a href="#">START</a><a href="#">ABOUT US</a><a href="#">SLA</a><a href="#">CREDITS</a></nav>
    <div class="footer-rule"></div>
    <div class="copyright">© 2021 coinnest7 Pool</div>
  </footer>

</div>
</body>
</html>
```